German Webagency needs fresh modern Design

Our website is 4 years old. We need an fresh modern website. All pics we used before are from customers or handmade by us. the new website should be clear with nice handling. please dont copy something from template websites. it would be great if you can surprise us with something great. its our first project here. don´t worry if i make a mistake in responding or briefing. after 20 years you can´t see the works of your own "designer" so we hope for help :-)
our existing site: www.tovankreativ.de
Target Market(s)
small and middle sized companys in germany
Number of Pages Required
4 page
Font styles to use
Colors
Designer to choose colors to be used in the design.
Requirements
Must have
- Responsive (sure we code it)
- Modern and big Font ..Headlines and Slider
- innovative..if you know something new..feel free to show
Nice to have
- the site with our works/refences should look great and later easy to handle when we code it or use wp.
- we like black and grey but if you have better ideas also feel free
Should not have
- a cup of coffe..laptop.. a pencil a handwritten font
- dont copy and modify templates from know websites..bad style

```html
<!DOCTYPE html>
<html lang="de">
<head>
<meta charset="utf-8">
<title>tovankreativ – Webagentur</title>
<link href="https://fonts.googleapis.com/css2?family=Oswald:wght@300;400&family=Roboto+Condensed:wght@300;400&family=Open+Sans:wght@400;600;700&display=swap" rel="stylesheet">
<style>
  :root{
    --page-bg:#f1f1f1;
    --bar-dark:#2a2b2c;
    --strip-dark:#221f20;
    --white:#ffffff;
    --brand-blue:#3a87cc;
    --nav-blue:#1f4f86;
    --btn-navy:#1d4a78;
    --content-bg:#e3e4e6;
    --text-grey:#555a60;
    --ink:#1c1c1c;
    --line:#2b2b2b;
  }
  *{margin:0;padding:0;box-sizing:border-box}
  html,body{width:1200px;height:1200px;overflow:hidden;background:var(--page-bg)}
  .site{position:absolute;left:172px;top:68px;width:874px;height:1088px;background:var(--bar-dark);box-shadow:0 6px 18px rgba(0,0,0,.35);font-family:"Open Sans",sans-serif}

  .topbar{position:absolute;left:0;top:0;width:100%;height:39px;color:var(--white);font-size:15px}
  .topbar .social{position:absolute;left:56px;top:9px;display:flex;gap:18px}
  .topbar .social span{display:flex;align-items:center;gap:6px}
  .dot{display:inline-block;width:9px;height:9px;border-radius:50%;background:var(--brand-blue)}
  .topbar .signin{position:absolute;right:65px;top:9px;font-size:15px}

  .navbox{position:absolute;left:22px;top:39px;width:828px;height:68px;background:var(--white)}
  .logo{position:absolute;left:14px;top:18px;font-family:"Open Sans",sans-serif;font-weight:700;font-size:26px;color:var(--brand-blue);letter-spacing:-.5px}
  .nav{position:absolute;left:269px;top:20px;display:flex;gap:20px;font-family:"Open Sans",sans-serif;font-size:19px;color:var(--nav-blue)}
  .nav .active{font-weight:700}
  .cta{position:absolute;left:674px;top:13px;width:127px;height:38px;background:var(--brand-blue);border-radius:4px;color:var(--white);padding:3px 6px;line-height:1.1}
  .cta small{display:block;font-size:10.5px;font-weight:600}
  .cta b{display:block;font-size:13.5px;letter-spacing:.5px}

  .hero{position:absolute;left:0;top:107px;width:874px;height:350px;background:radial-gradient(ellipse at 40% 55%,#5a6775 0%,#39434f 45%,#1f252c 100%)}
  .hero-inner{position:absolute;inset:0;color:var(--white);text-align:center}
  .hero .rule{position:absolute;height:1px;background:rgba(255,255,255,.8)}
  .hero .mark{position:absolute;left:0;width:100%;top:62px;font-family:"Oswald",sans-serif;font-size:15px;font-weight:300}
  .hero h1{position:absolute;left:0;width:100%;top:82px;font-family:"Oswald",sans-serif;font-weight:300;font-size:42px;letter-spacing:.5px}
  .hero .sub{position:absolute;left:0;width:100%;top:170px;font-family:"Oswald",sans-serif;font-weight:300;font-size:20px}
  .dots{position:absolute;left:0;width:100%;top:321px;display:flex;justify-content:center;gap:5px}
  .dots i{width:15px;height:15px;border-radius:50%;border:1.5px solid var(--white)}
  .dots i.on{background:var(--white)}

  .welcome{position:absolute;left:0;top:457px;width:874px;height:471px;background:var(--content-bg)}
  .portrait{position:absolute;left:56px;top:43px;width:220px;height:360px;background:linear-gradient(180deg,#8e96a8 0%,#a9b1c3 55%,rgba(227,228,230,0) 100%);border-radius:80px 80px 0 0}
  .welcome h2{position:absolute;left:344px;top:58px;font-family:"Oswald",sans-serif;font-weight:300;font-size:35px;color:var(--ink);letter-spacing:.5px}
  .welcome h2 span{color:var(--brand-blue)}
  .h-rule{position:absolute;left:344px;top:108px;width:296px;height:1px;background:#9a9ea3}
  .thumb{position:absolute;left:340px;top:131px;width:146px;height:97px;background:linear-gradient(135deg,#2e3f56,#5b6a7d)}
  .copy{font-family:"Roboto Condensed",sans-serif;font-weight:300;color:var(--text-grey);font-size:13px;letter-spacing:-.25px}
  .copy span{display:block;white-space:nowrap;text-align:justify;text-align-last:justify}
  .copy span.last{text-align-last:left}
  .copy.side{position:absolute;left:501px;top:131px;width:290px;line-height:20px}
  .copy.line{position:absolute;left:347px;top:248px;white-space:nowrap}
  .copy.wide{position:absolute;left:344px;top:277px;width:454px;line-height:21.6px}
  .btn{position:absolute;left:345px;top:350px;width:105px;height:35px;background:var(--btn-navy);color:var(--white);font-family:"Oswald",sans-serif;font-weight:300;font-size:19px;text-align:center;line-height:35px}
  .corner{position:absolute;left:0;top:0}

  .footer{position:absolute;left:0;top:928px;width:874px;height:120px;color:var(--white)}
  .footer .icons{position:absolute;left:0;width:100%;top:37px;display:flex;justify-content:center;gap:18px}
  .footer .icons i{width:24px;height:24px;border-radius:50%;background:var(--white)}
  .footer .contact{position:absolute;left:0;width:100%;top:74px;text-align:center;font-family:"Oswald",sans-serif;font-weight:300;font-size:19px}
  .footer .contact span{color:var(--brand-blue)}
  .legal{position:absolute;left:0;top:1048px;width:874px;height:40px;background:var(--strip-dark);color:var(--white);font-size:10px;text-align:center;line-height:38px}
</style>
</head>
<body>
<div class="site">
  <div class="topbar">
    <div class="social">
      <span><i class="dot"></i>tovankreativ</span>
      <span><i class="dot"></i>tovankreativ</span>
    </div>
    <div class="signin">SIGN IN</div>
  </div>

  <header class="navbox">
    <div class="logo">tovankreativ.de</div>
    <nav class="nav">
      <span class="active">Home</span><span>About Us</span><span>Services</span><span>Contact</span>
    </nav>
    <div class="cta"><small>Make An Appoinment</small><b>05123 - 400 218</b></div>
  </header>

  <section class="hero" role="img" aria-label="Hände auf einer Laptop-Tastatur mit überlagerten digitalen Symbolen">
    <div class="hero-inner">
      <div class="rule" style="left:97px;top:73px;width:304px"></div>
      <div class="rule" style="left:462px;top:73px;width:318px"></div>
      <div class="mark">x X x</div>
      <h1>IDEEN &amp; VISIONEN GEMEINSAM VERWIRKLICHEN</h1>
      <div class="rule" style="left:89px;top:150px;width:691px"></div>
      <div class="sub">Neue Märkte &nbsp;•&nbsp; Mehr Umsatz &nbsp;•&nbsp; Neue Kunden</div>
      <div class="dots"><i class="on"></i><i></i><i></i><i></i></div>
    </div>
  </section>

  <section class="welcome">
    <svg class="corner" width="874" height="471" aria-hidden="true">
      <polyline points="706,29 826,29 826,149" fill="none" stroke="#2b2b2b" stroke-width="1"/>
      <circle cx="706" cy="29" r="2" fill="#2b2b2b"/><circle cx="826" cy="149" r="2" fill="#2b2b2b"/>
      <polyline points="55,331 55,444 169,444" fill="none" stroke="#2b2b2b" stroke-width="1"/>
      <circle cx="55" cy="331" r="2" fill="#2b2b2b"/><circle cx="169" cy="444" r="2" fill="#2b2b2b"/>
    </svg>
    <div class="portrait" role="img" aria-label="Geschäftsfrau mit Tablet in der Hand"></div>
    <h2><span>Welcome to</span> Our website</h2>
    <div class="h-rule"></div>
    <div class="thumb" role="img" aria-label="Zwei Kolleginnen arbeiten gemeinsam am Bildschirm"></div>
    <p class="copy side">
      <span>Lorem Ipsum is simply dummy text of the printing and</span>
      <span>typesetting industry. Lorem Ipsum has been the industry's</span>
      <span>standard dummy text ever since the 1500s, when an</span>
      <span>unknown printer took a galley of type and scrambled it to</span>
      <span class="last">make a type specimen book.</span>
    </p>
    <p class="copy line">took a galley of type and scrambled it to make a type specimen book.</p>
    <p class="copy wide">
      <span>Lorem Ipsum is simply dummy text of the printing and typesetting industry. Lorem Ipsum</span>
      <span>has been the industry's standard dummy text ever since the 1500s, when an unknown</span>
      <span class="last">printer took a galley of type and scrambled it to make a type specimen book.</span>
    </p>
    <div class="btn">READ MORE</div>
  </section>

  <footer class="footer">
    <div class="icons"><i></i><i></i><i></i></div>
    <div class="contact"><span>Tel :</span> 05123 - 400 218 &nbsp;| <span>Fax :</span> 05123 - 77 31 09 | <span>Mobil :</span> 0171 - 23 45 678</div>
  </footer>
  <div class="legal">Impressum | Datenschutz | © TOVANkreativ</div>
</div>
</body>
</html>
```